依頼詳細
法人のお客様も多くなった為
しっかりとした印象を持って頂けるような名刺へ
デザインを新しくしたいと思っています。
誠実さが伝わるスタイリッシュなデザインが希望です。
配色・横型・縦型お任せします。

ロゴデータは添付ファイルにアップロードさせて頂きますので
そちらをご利用ください。

印刷は、スリーネスト等に依頼を考えておりますので
そのまま入稿出来るデータで頂けますと幸いです。
記載項目
会社名:萩森電機
役職:代表
保有資格:第一種電気工事士(認定番号)
消防設備士(認定番号)
防犯設備士(認定番号)
など3つ程記載したいと思います。

氏名:
住所:
電話:
FAX:
Mail:

事業内容
一般電気工事(一般住宅・マンション・店舗・工場)
空調・エアコン工事
通信設備工事(インターネット・電話)
防犯設備工事(防犯カメラ・マンションインターホン・電気錠)
LED照明工事(一般住宅・マンション・店舗・工場・スタジアム照明)
映像・音響設備工事
希望イメージ
シンプル 複雑
単色 カラフル
暗い 明るい
日常 高級
遊び心 厳粛
未来的 伝統的
女性的 男性的
希望する色
納品ファイル
• 高解像度JPG (.jpg)
• イラストレーター形式 (.ai)
• フォトショップ形式 (.psd)
• PNG形式 (.png)
補足説明
募集開始から1日しか経っておりませんが
早くも多数のご提案を頂きありがとうございます。
大変素晴らしいデザインが多く
お気に入りに入れたい物も御座いますが
様々なご提案を拝見させて頂きたいので
デザインの偏りを防ぐ為にもあえてお気に入りは入れずに
拝見させて頂きます。

早々にご提案頂きましたデザイナー様には
しばらくお待ち頂くことになりますが
何卒よろしくお願い申し上げます。

※素晴らしいデザインが多い為、選定確約に変更させて頂きます。
引き続きたくさんのご提案ありがとうございます。

印刷の依頼先ですが、スリーネスト以外も検討しておりまして
名刺ルミと言うサイトも検討しております。
スリーネストでは出来ない、エンボス、デボス加工等も可能な印刷屋さんになりますので
エンボス、デボス加工を使ったデザインも募集します。

加工一覧、及びデータ作成時の注意事項のリンクを
貼っておきますので、ご確認頂けましたら幸いです。

名刺ルミ加工一覧↓
https://www.meishilumi.jp/Info/Aftercutinfo05

引き続き宜しくお願い致します。
追記です。

用紙はヴァンヌーボーVホワイト215kg
印刷方法はオフセット印刷の予定です。

宜しくお願い致します。
■ 選んだ理由

本当に素晴らしいデザインも多く悩みましたが
ロゴのデザインや配色が決まっていた為、似たようなデザインが多くなりがちな中
裏面の事業内容のデザインに、インパクトのある特徴的なデザインをして頂いた
tobio様のデザインを採用させて頂きました。
度重なる修正にもいつも迅速にご対応頂き感謝しております。
この度は、本当に有難う御座いました。

■ 提案者全員のお礼・コメント

本当に沢山のご提案を頂きました皆様、ありがとうございました。
素晴らしいデザインも多く、複数のデザインの名刺を作ろうかと悩んだ程です。
また、何かご縁が御座いましたら
その時は何卒よろしくお願い申し上げます。

この度は、皆様本当にありがとうございました。

```html
<!DOCTYPE html>
<html lang="ja">
<head>
<meta charset="utf-8">
<title>萩森電機 名刺デザイン</title>
<link rel="stylesheet" href="https://fonts.googleapis.com/css2?family=Noto+Sans+JP:wght@400;500;700&family=Roboto:wght@400&display=swap">
<style>
  :root {
    --bg: #dcdcdc;
    --label: #555555;
    --navy: #0d3f8f;
    --blue: #1565c8;
    --ink: #333333;
    --muted: #666666;
    --paper: #ffffff;
  }
  * { margin: 0; padding: 0; box-sizing: border-box; }
  html, body { width: 805px; height: 1200px; overflow: hidden; background: var(--bg); }
  body { position: relative; font-family: "Noto Sans JP", sans-serif; color: var(--ink); }

  .side-label { position: absolute; left: 54px; font-family: "Roboto", sans-serif; font-size: 20px; color: var(--label); }
  .side-label--front { top: 70px; }
  .side-label--back { top: 642px; }

  .card { position: absolute; left: 54px; width: 703px; height: 432px; overflow: hidden; box-shadow: 0 2px 6px rgba(0,0,0,.25); }
  .card--front { top: 113px; background: var(--paper); }
  .card--back { top: 690px; background: linear-gradient(135deg, #0a3a8a 0%, #1560c4 55%, #0c4aa6 100%); }
  .card svg.decor { position: absolute; inset: 0; }

  /* front */
  .title { position: absolute; left: 150px; top: 72px; font-size: 14px; letter-spacing: 4px; }
  .name { position: absolute; left: 150px; top: 98px; font-size: 27px; font-weight: 700; letter-spacing: 5px; color: #222; line-height: 40px; white-space: nowrap; }
  .name-roman { font-family: "Roboto", sans-serif; font-size: 13px; font-weight: 400; letter-spacing: 0; margin-left: 10px; color: var(--muted); }
  .name-rule { position: absolute; left: 150px; top: 144px; width: 250px; height: 1px; background: #888; }
  .licenses { position: absolute; left: 150px; top: 156px; list-style: none; font-size: 10px; line-height: 19px; color: var(--muted); }

  .brand { position: absolute; left: 500px; top: 114px; display: flex; align-items: center; gap: 10px; }
  .brand-mark { width: 18px; height: 18px; background: var(--blue); }
  .brand-name { font-size: 22px; font-weight: 700; color: var(--navy); letter-spacing: 2px; }

  .company { position: absolute; left: 262px; top: 282px; font-size: 19px; font-weight: 500; color: #222; }
  .contact { position: absolute; left: 262px; top: 314px; list-style: none; font-size: 13px; line-height: 26px; }
  .contact li { display: flex; align-items: center; gap: 8px; white-space: nowrap; }
  .contact svg { width: 15px; height: 15px; flex: none; }
  .contact .pair { margin-left: 14px; display: inline-flex; align-items: center; gap: 8px; }

  /* back */
  .back-brand { position: absolute; left: 62px; top: 122px; display: flex; align-items: center; gap: 12px; }
  .back-brand__mark { width: 20px; height: 20px; background: var(--paper); }
  .back-brand__name { font-size: 30px; font-weight: 700; letter-spacing: 4px; color: var(--paper); }
  .services-rule { position: absolute; left: 346px; top: 62px; width: 2px; height: 262px; background: var(--paper); }
  .services { position: absolute; left: 370px; top: 66px; list-style: none; color: var(--paper); }
  .services li { margin-bottom: 7px; }
  .service-name { display: flex; align-items: center; gap: 8px; font-size: 14px; font-weight: 700; line-height: 20px; }
  .service-name::before { content: ""; width: 7px; height: 7px; background: var(--paper); }
  .service-detail { display: block; font-size: 10px; line-height: 15px; margin-left: 15px; opacity: .9; }
</style>
</head>
<body>
  <p class="side-label side-label--front">Front</p>
  <section class="card card--front">
    <svg class="decor" viewBox="0 0 703 432" preserveAspectRatio="none" aria-hidden="true">
      <path d="M0 0 H105 C55 120 135 260 35 432 H0 Z" fill="#1565c8"/>
      <path d="M0 0 H65 C20 130 95 270 0 390 Z" fill="#0d3f8f"/>
      <path d="M105 0 C60 120 150 260 50 432" fill="none" stroke="#7fb6ee" stroke-width="3"/>
      <path d="M125 0 C85 130 170 270 80 432" fill="none" stroke="#bcd8f5" stroke-width="1.5"/>
    </svg>
    <p class="title">代表</p>
    <h1 class="name">萩森 健一<span class="name-roman">Kenichi Hagimori</span></h1>
    <div class="name-rule"></div>
    <ul class="licenses">
      <li>第一種電気工事士（認定番号）</li>
      <li>消防設備士（認定番号）</li>
      <li>防犯設備士（認定番号）</li>
    </ul>
    <div class="brand">
      <span class="brand-mark"></span>
      <span class="brand-name">萩森電機</span>
    </div>
    <p class="company">萩森電機</p>
    <ul class="contact">
      <li>
        <svg viewBox="0 0 16 16" aria-hidden="true"><rect width="16" height="16" rx="3" fill="#1565c8"/><path d="M8 3 L13 7.5 H11.5 V13 H4.5 V7.5 H3 Z" fill="#fff"/></svg>
        〒123-0000 東京都○○○○1-2-34○○○○
      </li>
      <li>
        <svg viewBox="0 0 16 16" aria-hidden="true"><rect width="16" height="16" rx="3" fill="#1565c8"/><path d="M5 3 C4 4 4 6 6 9 C8 12 10 13 11.5 12.5 L12.5 11 L10.5 9.5 L9.5 10.5 C8.5 10 6.5 8 6 7 L7 6 L5.7 3.5 Z" fill="#fff"/></svg>
        03-0000-0000
        <span class="pair">
          <svg viewBox="0 0 16 16" aria-hidden="true"><rect width="16" height="16" rx="3" fill="#1565c8"/><rect x="3" y="6" width="10" height="6" fill="#fff"/><rect x="5" y="3" width="6" height="3" fill="#fff"/></svg>
          03-0000-0000
        </span>
      </li>
      <li>
        <svg viewBox="0 0 16 16" aria-hidden="true"><rect width="16" height="16" rx="3" fill="#1565c8"/><rect x="3" y="4.5" width="10" height="7" fill="#fff"/><path d="M3 4.5 L8 8.5 L13 4.5" fill="none" stroke="#1565c8" stroke-width="1"/></svg>
        info@example.com
      </li>
    </ul>
  </section>

  <p class="side-label side-label--back">Back</p>
  <section class="card card--back">
    <svg class="decor" viewBox="0 0 703 432" preserveAspectRatio="none" aria-hidden="true">
      <path d="M0 300 C200 240 420 300 703 200 V432 H0 Z" fill="#0a3a8a" opacity=".45"/>
      <path d="M0 280 C220 210 430 280 703 170" fill="none" stroke="#ffffff" stroke-opacity=".35" stroke-width="2"/>
      <path d="M0 310 C230 250 440 310 703 210" fill="none" stroke="#ffffff" stroke-opacity=".2" stroke-width="1.5"/>
    </svg>
    <div class="back-brand">
      <span class="back-brand__mark"></span>
      <span class="back-brand__name">萩森電機</span>
    </div>
    <div class="services-rule"></div>
    <ul class="services">
      <li><span class="service-name">一般電気工事</span><span class="service-detail">一般住宅・マンション・店舗・工場</span></li>
      <li><span class="service-name">通信設備工事</span><span class="service-detail">インターネット・電話</span></li>
      <li><span class="service-name">空調・エアコン工事</span></li>
      <li><span class="service-name">防犯設備工事</span><span class="service-detail">防犯カメラ・マンションインターホン・電気錠</span></li>
      <li><span class="service-name">LED 照明工事</span><span class="service-detail">一般住宅・マンション・店舗・工場・スタジアム照明</span></li>
      <li><span class="service-name">映像・音響設備工事</span></li>
    </ul>
  </section>
</body>
</html>
```